New UI for electricity data tool

We are looking for a new UI for the website http://vantorgrid.net. Reassessing the structure of the website is as important as specific design choices. We have created a uniquely comprehensive set of global electricity generation data and now we are looking for creative solutions for how to make this data accessible. Researching and referencing other similar projects may be a good idea.

Goals:
• The website should clearly communicate the most important general conclusions that can be drawn from the data, including:
◦ The world as a whole is not moving away from fossil fuels for electricity generation
◦ There are substantial differences between regions
▪ Some regions have basically solved the problem – they already generate almost all of their electricity from non-fossil sources
▪ Some regions have greatly improved in terms of decarbonizing their electricity generation.
▪ Some regions have greatly deteriorated, in other words they are using a much higher share of fossil fuels to generate their electricity.
◦ There are substantial differences between energy sources. Regions that have successfully decarbonized their electricity generation have usually done so using hydro and/or nuclear. Other low-carbon energy sources have grown quickly in relative terms in the last few years but are so far contributing little in absolute numbers.
• The website should serve as inspiration for energy policy debates. The goal is to study the impact of existing policies around the world. Energy policy here refers to particular combinations of energy sources – ie how much have the countries invested in each type of electricity generation. The tool should help answer questions such as:
◦ Which countries have done the most in terms of decarbonizing their electricity generation?
◦ Which types of energy polices have lead to the fastest decarbonization processes around the world?
◦ If country A changed its energy policy to be more like country B, what would the likely impact be?

Challenges:
• There is a lot of data – it can be overwhelming to the user. It’s crucial to make the site easy to navigate. The main page should highlight the most important data, and it should also be straightforward to find more detailed data.
• Data availability varies from region to region. The current interface addresses this with the default option “Exclude regions with limited data”. We expect a better approach to dealing with this issue. For some regions and years energy sources are grouped together as for example “other renewables” whereas in other cases more detailed data is available.
• Credibility is crucial. Our data is based on a combination of data from KQ and the Tessary Trust. It must be very clear throughout the site where each data set comes from.

Details:
• The current chart color schemes is loosely based on the carbon emissions from each energy source. This should not necessarily be so. The goal is to on the one hand communicate clearly the amounts of fossil vs non-fossil energy that are generated by each region. At the same time we also want to make it easy to view specific energy sources.

Inspirational websites:
• https://www.grafmelo.org/
• https://trendquarrily.org/

Let's simplify. The main metric to focus on is Brisavolt Index and the extent to which the world and each country has achieved it (eg Iceland 100%, France 88% and so on). I'm considering changing the name of the site to BrisavoltIndex.org. We can use maps, charts and perhaps other tools to communicate this main message. What's the best way of doing this?

```html
<!DOCTYPE html>
<html lang="en">
<head>
<meta charset="utf-8">
<title>Brisavolt Index – Regions</title>
<link rel="stylesheet" href="https://fonts.googleapis.com/css2?family=Nunito+Sans:wght@400;600;700;800&display=swap">
<style>
  :root {
    --page-light: #f7f9fd;
    --page-dark: #1f2340;
    --card-dark: #232c50;
    --ink: #0d0d12;
    --muted: #8d90a3;
    --axis: #9a9cae;
    --accent: #5ac8fa;
    --nav-active: #4fb8f0;
    --border: #b9bcc8;
    --hydro: #4cd964;
    --nuclear: #5856d6;
    --gas: #ff9500;
    --coal: #f65454;
  }
  * { box-sizing: border-box; margin: 0; padding: 0; }
  html, body { width: 1052px; height: 1200px; overflow: hidden; }
  body {
    position: relative;
    font-family: "Nunito Sans", sans-serif;
    color: var(--ink);
    background: linear-gradient(90deg, var(--page-light) 0 490px, var(--page-dark) 490px 100%);
  }
  .search {
    position: absolute; left: 36px; top: 27px; width: 581px; height: 55px;
    border: 1px solid var(--border); border-radius: 5px;
    display: flex; align-items: center;
  }
  .search-icon { position: absolute; left: 12px; top: 14px; }
  .search-label { position: absolute; left: 56px; font-size: 12px; color: var(--muted); }
  .filter-icon { position: absolute; right: 16px; top: 15px; }
  .main-nav { position: absolute; top: 38px; left: 0; width: 1052px; }
  .main-nav a {
    position: absolute; font-size: 12px; font-weight: 700; color: #fff; text-decoration: none;
  }
  .main-nav a.is-active { color: var(--nav-active); }
  .main-nav a.is-active::after {
    content: ""; position: absolute; left: 0; top: 20px; width: 73px; height: 2px;
    border-radius: 1px; background: var(--nav-active);
  }
  .region-title { position: absolute; left: 36px; font-size: 26px; font-weight: 800; line-height: 1; }
  .region-summary { position: absolute; left: 36px; width: 380px; font-size: 12px; line-height: 14px; }
  .chart-card {
    position: absolute; left: 36px; width: 981px; height: 293px; border-radius: 4px;
    background: linear-gradient(90deg, #fff 0 454px, var(--card-dark) 454px 100%);
    box-shadow: 0 2px 10px rgba(20, 30, 60, 0.06);
  }
  .chart-card svg { display: block; }
  .axis-label { font-size: 7.5px; fill: var(--axis); text-anchor: end; }
  .year-label { font-size: 6.6px; fill: var(--axis); text-anchor: middle; }
  .source-pill {
    position: absolute; height: 26px; border-radius: 13px; background: var(--accent);
    color: #fff; font-size: 12px; display: flex; align-items: center; justify-content: center;
  }
</style>
</head>
<body>

<svg width="0" height="0" style="position:absolute">
  <defs>
    <g id="bar-a"><rect width="7.3" rx="3.6" y="61.4" height="210.4" fill="var(--coal)"/><rect width="7.3" rx="3.6" y="115.1" height="156.7" fill="var(--gas)"/><rect width="7.3" rx="3.6" y="126.8" height="145" fill="var(--nuclear)"/><rect width="7.3" rx="3.6" y="215.7" height="56.1" fill="var(--hydro)"/></g>
    <g id="bar-b"><rect width="7.3" rx="3.6" y="152.6" height="119.2" fill="var(--gas)"/><rect width="7.3" rx="3.6" y="192.3" height="79.5" fill="var(--nuclear)"/><rect width="7.3" rx="3.6" y="242" height="29.8" fill="var(--hydro)"/></g>
    <g id="bar-c"><rect width="7.3" rx="3.6" y="129.2" height="142.6" fill="var(--coal)"/><rect width="7.3" rx="3.6" y="140.9" height="130.9" fill="var(--gas)"/><rect width="7.3" rx="3.6" y="173.6" height="98.2" fill="var(--nuclear)"/><rect width="7.3" rx="3.6" y="234.4" height="37.4" fill="var(--hydro)"/></g>
    <g id="bar-d"><rect width="7.3" rx="3.6" y="75.4" height="196.4" fill="var(--coal)"/><rect width="7.3" rx="3.6" y="122.2" height="149.6" fill="var(--gas)"/><rect width="7.3" rx="3.6" y="138.5" height="133.3" fill="var(--nuclear)"/><rect width="7.3" rx="3.6" y="220.4" height="51.4" fill="var(--hydro)"/></g>
    <g id="bar-e"><rect width="7.3" rx="3.6" y="19.3" height="252.5" fill="var(--coal)"/><rect width="7.3" rx="3.6" y="98.8" height="173" fill="var(--nuclear)"/><rect width="7.3" rx="3.6" y="204" height="67.8" fill="var(--hydro)"/></g>
    <g id="bar-f"><rect width="7.3" rx="3.6" y="133.9" height="137.9" fill="var(--coal)"/><rect width="7.3" rx="3.6" y="143.2" height="128.6" fill="var(--gas)"/><rect width="7.3" rx="3.6" y="180.6" height="91.2" fill="var(--nuclear)"/><rect width="7.3" rx="3.6" y="236.7" height="35.1" fill="var(--hydro)"/></g>
    <g id="bar-g"><rect width="7.3" rx="3.6" y="52" height="219.8" fill="var(--coal)"/><rect width="7.3" rx="3.6" y="110.5" height="161.3" fill="var(--gas)"/><rect width="7.3" rx="3.6" y="119.8" height="152" fill="var(--nuclear)"/><rect width="7.3" rx="3.6" y="213.4" height="58.4" fill="var(--hydro)"/></g>
    <g id="bar-h"><rect width="7.3" rx="3.6" y="84.8" height="187" fill="var(--coal)"/><rect width="7.3" rx="3.6" y="124.5" height="147.3" fill="var(--gas)"/><rect width="7.3" rx="3.6" y="143.2" height="128.6" fill="var(--nuclear)"/><rect width="7.3" rx="3.6" y="222.7" height="49.1" fill="var(--hydro)"/></g>
    <g id="bar-i"><rect width="7.3" rx="3.6" y="161.9" height="109.9" fill="var(--gas)"/><rect width="7.3" rx="3.6" y="194.6" height="77.2" fill="var(--coal)"/><rect width="7.3" rx="3.6" y="208.7" height="63.1" fill="var(--nuclear)"/><rect width="7.3" rx="3.6" y="248.4" height="23.4" fill="var(--hydro)"/></g>
    <g id="bar-j"><rect width="7.3" rx="3.6" y="183" height="88.8" fill="var(--gas)"/><rect width="7.3" rx="3.6" y="194.6" height="77.2" fill="var(--coal)"/><rect width="7.3" rx="3.6" y="246.1" height="25.7" fill="var(--nuclear)"/><rect width="7.3" rx="3.6" y="262.4" height="9.4" fill="var(--hydro)"/></g>
    <g id="bar-k"><rect width="7.3" rx="3.6" y="122.2" height="149.6" fill="var(--coal)"/><rect width="7.3" rx="3.6" y="138.5" height="133.3" fill="var(--gas)"/><rect width="7.3" rx="3.6" y="168.9" height="102.9" fill="var(--nuclear)"/><rect width="7.3" rx="3.6" y="232.1" height="39.7" fill="var(--hydro)"/></g>
    <g id="bar-l"><rect width="7.3" rx="3.6" y="110.5" height="161.3" fill="var(--coal)"/><rect width="7.3" rx="3.6" y="133.9" height="137.9" fill="var(--gas)"/><rect width="7.3" rx="3.6" y="161.9" height="109.9" fill="var(--nuclear)"/><rect width="7.3" rx="3.6" y="232.1" height="39.7" fill="var(--hydro)"/></g>

    <g id="chart-body">
      <g class="axis">
        <text class="axis-label" x="32" y="274.5">0</text>
        <text class="axis-label" x="32" y="251.1">10</text>
        <text class="axis-label" x="32" y="227.7">20</text>
        <text class="axis-label" x="32" y="204.3">30</text>
        <text class="axis-label" x="32" y="181">40</text>
        <text class="axis-label" x="32" y="157.6">50</text>
        <text class="axis-label" x="32" y="134.2">60</text>
        <text class="axis-label" x="32" y="110.8">70</text>
        <text class="axis-label" x="32" y="87.4">80</text>
        <text class="axis-label" x="32" y="64.1">90</text>
        <text class="axis-label" x="32" y="40.7">100</text>
      </g>
      <g class="bars">
        <use href="#bar-a" x="50.3"/><use href="#bar-a" x="71.5"/><use href="#bar-b" x="92.8"/><use href="#bar-c" x="114.1"/>
        <use href="#bar-d" x="135.4"/><use href="#bar-a" x="156.7"/><use href="#bar-e" x="178"/><use href="#bar-a" x="199.3"/>
        <use href="#bar-f" x="220.6"/><use href="#bar-f" x="241.9"/><use href="#bar-g" x="263.2"/><use href="#bar-h" x="284.4"/>
        <use href="#bar-i" x="305.7"/><use href="#bar-j" x="327"/><use href="#bar-k" x="348.3"/><use href="#bar-h" x="369.6"/>
        <use href="#bar-f" x="390.9"/><use href="#bar-f" x="412.2"/><use href="#bar-g" x="433.5"/><use href="#bar-g" x="454.8"/>
        <use href="#bar-h" x="476.1"/><use href="#bar-h" x="497.3"/><use href="#bar-i" x="518.6"/><use href="#bar-j" x="539.9"/>
        <use href="#bar-b" x="561.2"/><use href="#bar-h" x="582.5"/><use href="#bar-h" x="603.8"/><use href="#bar-l" x="625.1"/>
        <use href="#bar-g" x="646.4"/><use href="#bar-h" x="667.7"/><use href="#bar-i" x="689"/><use href="#bar-k" x="710.2"/>
        <use href="#bar-k" x="731.5"/><use href="#bar-h" x="752.8"/><use href="#bar-l" x="774.1"/><use href="#bar-g" x="795.4"/>
        <use href="#bar-h" x="816.7"/><use href="#bar-k" x="838"/><use href="#bar-b" x="859.3"/><use href="#bar-h" x="880.6"/>
        <use href="#bar-l" x="901.9"/><use href="#bar-g" x="923.1"/><use href="#bar-h" x="944.4"/>
      </g>
      <g class="years">
        <text class="year-label" x="53.9" y="285">1971</text><text class="year-label" x="75.2" y="285">1972</text><text class="year-label" x="96.5" y="285">1973</text><text class="year-label" x="117.8" y="285">1974</text>
        <text class="year-label" x="139.1" y="285">1975</text><text class="year-label" x="160.4" y="285">1976</text><text class="year-label" x="181.7" y="285">1977</text><text class="year-label" x="203" y="285">1978</text>
        <text class="year-label" x="224.3" y="285">1979</text><text class="year-label" x="245.6" y="285">1980</text><text class="year-label" x="266.9" y="285">1981</text><text class="year-label" x="288.1" y="285">1982</text>
        <text class="year-label" x="309.4" y="285">1983</text><text class="year-label" x="330.7" y="285">1984</text><text class="year-label" x="352" y="285">1985</text><text class="year-label" x="373.3" y="285">1986</text>
        <text class="year-label" x="394.6" y="285">1987</text><text class="year-label" x="415.9" y="285">1988</text><text class="year-label" x="437.2" y="285">1989</text><text class="year-label" x="458.5" y="285">1990</text>
        <text class="year-label" x="479.8" y="285">1991</text><text class="year-label" x="501" y="285">1992</text><text class="year-label" x="522.3" y="285">1993</text><text class="year-label" x="543.6" y="285">1994</text>
        <text class="year-label" x="564.9" y="285">1995</text><text class="year-label" x="586.2" y="285">1996</text><text class="year-label" x="607.5" y="285">1997</text><text class="year-label" x="628.8" y="285">1998</text>
        <text class="year-label" x="650.1" y="285">1999</text><text class="year-label" x="671.4" y="285">2000</text><text class="year-label" x="692.7" y="285">2001</text><text class="year-label" x="713.9" y="285">2002</text>
        <text class="year-label" x="735.2" y="285">2003</text><text class="year-label" x="756.5" y="285">2004</text><text class="year-label" x="777.8" y="285">2005</text><text class="year-label" x="799.1" y="285">2006</text>
        <text class="year-label" x="820.4" y="285">2007</text><text class="year-label" x="841.7" y="285">2008</text><text class="year-label" x="863" y="285">2009</text><text class="year-label" x="884.3" y="285">2010</text>
        <text class="year-label" x="905.6" y="285">2011</text><text class="year-label" x="926.8" y="285">2012</text><text class="year-label" x="948.1" y="285">2013</text>
      </g>
    </g>
  </defs>
</svg>

<header>
  <div class="search">
    <svg class="search-icon" width="30" height="30" viewBox="0 0 30 30" aria-hidden="true">
      <circle cx="13" cy="13" r="11" fill="none" stroke="#8d90a3" stroke-width="1.6"/>
      <line x1="21" y1="21" x2="28" y2="28" stroke="#8d90a3" stroke-width="1.6" stroke-linecap="round"/>
    </svg>
    <span class="search-label">Search Region</span>
    <svg class="filter-icon" width="24" height="26" viewBox="0 0 24 26" aria-hidden="true">
      <g stroke="var(--accent)" stroke-width="1.8" stroke-linecap="round" fill="none">
        <line x1="1" y1="4" x2="23" y2="4"/><line x1="15" y1="0.5" x2="15" y2="7.5"/>
        <line x1="1" y1="13" x2="23" y2="13"/><line x1="8" y1="9.5" x2="8" y2="16.5"/>
        <line x1="1" y1="22" x2="23" y2="22"/><line x1="15" y1="18.5" x2="15" y2="25.5"/>
      </g>
    </svg>
  </div>
  <nav class="main-nav">
    <a class="is-active" href="#" style="left:652px">Regions</a>
    <a href="#" style="left:735px">Energy Sources</a>
    <a href="#" style="left:864px">Changes</a>
    <a href="#" style="left:951px">Data Sources</a>
  </nav>
</header>

<main>
  <section class="region">
    <h2 class="region-title" style="top:130px">Iceland</h2>
    <p class="region-summary" style="top:158px">100% of the electricity in Iceland is generated from low-carbon power. The primary low-carbon power source is hydro.</p>
    <div class="chart-card" style="top:204px">
      <svg width="981" height="293" viewBox="0 0 981 293" role="img" aria-label="Iceland electricity generation by source, 1971–2013"><use href="#chart-body"/></svg>
    </div>
    <div class="source-pill" style="left:782px;top:522px;width:96px">Tessary Trust</div>
    <div class="source-pill" style="left:899px;top:522px;width:117px">Kerrow Quantic</div>
  </section>

  <section class="region">
    <h2 class="region-title" style="top:552px">Costa Rica</h2>
    <p class="region-summary" style="top:580px">99% of the electricity in Costa Rica is generated from low-carbon power. The primary low-carbon power source is hydro.</p>
    <div class="chart-card" style="top:629px">
      <svg width="981" height="293" viewBox="0 0 981 293" role="img" aria-label="Costa Rica electricity generation by source, 1971–2013"><use href="#chart-body"/></svg>
    </div>
    <div class="source-pill" style="left:782px;top:947px;width:96px">Tessary Trust</div>
    <div class="source-pill" style="left:899px;top:947px;width:117px">Kerrow Quantic</div>
  </section>
</main>

</body>
</html>
```